依頼詳細
・余白のある、落ち着いたデザインを希望です。
・以下参考サイトのような色味(キーカラー)を希望です。
(デザインは極端に類似しないことが望ましい)
- https://rinpa-kissa.jp/
- https://hamonoya.com/
・サイトのメニューは
-ごあいさつ
-会社案内・沿革
-事業内容
-納入実績
-お問い合わせ
-みなせのものづくり(ブログ)
-ネットショップ
となる予定です。
この度は、「TOPページのデザイン」と、上記「下層ページのベースデザイン」を依頼いたします。
・レスポンシブでスマートフォンにも対応させます。
・TOPページにはNEWS(お知らせ)欄が入る予定です。
・最終的に当方でWordPressにて構築します。
・参考サイトのイメージにとらわれない自由なデザインでもOKです。
ぜひ様々なアイデアをご提案下さい。
サイトURL
ページ数
2ページ
希望イメージ
シンプル 複雑
単色 カラフル
暗い 明るい
日常 高級
遊び心 厳粛
未来的 伝統的
女性的 男性的
希望する色
茶系、背景は白でお願いいたします。
納品ファイル
• 高解像度JPG (.jpg)
• イラストレーター形式 (.ai)
• フォトショップ形式 (.psd)
• PNG形式 (.png)
補足説明
資料と素材写真を添付いたします。
写真は今後差し替え予定なのでダミーとしてお使いください。

素材画像で購入が必要なものがある場合、「Pexel Vault (https://vault.pexelmart.com/jp/)」より選定下さい。当方で購入しますので、ご提案の際はカンプ画像を利用いただき、採用後には素材のURL or ファイル番号をお伝えいただきます。

その他ご不明な点がございましたら、お気軽にご連絡下さい。

シンプルで飽きの来ないデザインをクライアント様が気に入りました。

この度は本当にたくさんのご提案をいただきましてまことにありがとうございました。
どのデザインも素敵で、選ぶのに時間がかかりまして申し訳ございませんでした。
またの機会がございましたらご提案ください。改めて御礼申し上げます。

```html
<!DOCTYPE html>
<html lang="ja">
<head>
<meta charset="utf-8">
<title>水瀬きがた</title>
<link href="https://fonts.googleapis.com/css2?family=Shippori+Mincho:wght@400;500;700&family=Cormorant+Garamond:ital,wght@0,400;0,500;1,400&display=swap" rel="stylesheet">
<style>
:root{
  --ink:#2b2520;
  --sub:#6d645a;
  --line:#d8d2c6;
  --key:#a68a4f;
  --key-dark:#8a6f3a;
  --panel:#f1eee6;
  --dark:#2f2822;
  --white:#ffffff;
}
*{box-sizing:border-box;margin:0;padding:0}
html,body{width:1200px;height:5388px;overflow:hidden;background:var(--white)}
body{font-family:"Shippori Mincho",serif;color:var(--ink);position:relative}
.en{font-family:"Cormorant Garamond",serif;letter-spacing:.06em}
a{color:inherit;text-decoration:none}

/* header */
.site-header{position:absolute;top:0;left:0;width:1200px;height:72px;background:var(--white);display:flex;align-items:center;padding:0 40px;z-index:2}
.brand{display:flex;flex-direction:column}
.brand-name{font-size:26px;font-weight:700;letter-spacing:.18em;color:var(--ink)}
.brand-en{font-size:11px;color:var(--sub);margin-top:2px}
.global-nav{display:flex;gap:30px;margin-left:auto;font-size:14px;letter-spacing:.08em}
.btn-shop{margin-left:36px;background:var(--key);color:var(--white);font-size:14px;padding:10px 22px;letter-spacing:.12em}

/* hero */
.hero{position:absolute;top:72px;left:0;width:1200px;height:928px;
  background:
    radial-gradient(ellipse 420px 300px at 70% 30%,rgba(232,196,150,.75),transparent 70%),
    radial-gradient(ellipse 360px 260px at 38% 72%,rgba(214,168,120,.6),transparent 70%),
    radial-gradient(ellipse 500px 380px at 85% 85%,rgba(40,26,18,.75),transparent 70%),
    radial-gradient(ellipse 300px 500px at 5% 40%,rgba(52,34,22,.7),transparent 70%),
    linear-gradient(120deg,#3e2a1d 0%,#7b5a3e 35%,#a8845f 58%,#5b3f2b 100%)}
.hero::after{content:"";position:absolute;inset:0;background:linear-gradient(90deg,rgba(20,12,8,.45),rgba(20,12,8,0) 55%)}
.hero-copy{position:absolute;left:48px;top:280px;color:var(--white);z-index:1}
.hero-title{font-size:58px;font-weight:500;line-height:1.35;letter-spacing:.08em}
.hero-en{font-size:17px;margin-top:18px;line-height:1.5;font-style:italic}

/* intro */
.intro{position:absolute;top:1000px;left:0;width:1200px;height:420px}
.intro-lead{position:absolute;left:470px;top:36px;font-size:20px;letter-spacing:.2em}
.intro-lead strong{font-size:34px;font-weight:700;margin-left:18px;letter-spacing:.24em}
.intro-lead .en{display:block;font-size:13px;color:var(--sub);margin-top:6px}
.intro-photo{position:absolute;left:112px;top:140px;width:410px;height:230px;
  background:
    radial-gradient(ellipse 140px 60px at 55% 45%,rgba(240,238,232,.9),transparent 70%),
    radial-gradient(ellipse 120px 90px at 20% 75%,rgba(60,58,55,.7),transparent 70%),
    radial-gradient(ellipse 160px 80px at 85% 20%,rgba(80,78,74,.6),transparent 70%),
    linear-gradient(135deg,#7d7a76,#c9c5be 50%,#5e5a55)}
.intro-text{position:absolute;left:570px;top:120px;height:260px;width:510px;writing-mode:vertical-rl;font-size:15px;line-height:2.1;letter-spacing:.14em;color:var(--ink)}

/* craft band */
.craft{position:absolute;top:1420px;left:0;width:1200px;height:460px;
  background:
    radial-gradient(ellipse 300px 160px at 55% 70%,rgba(196,150,110,.55),transparent 70%),
    radial-gradient(ellipse 260px 140px at 78% 45%,rgba(170,128,92,.5),transparent 70%),
    linear-gradient(100deg,#1f1915 0%,#3d3027 40%,#6b5544 72%,#2e241d 100%)}
.craft-copy{position:absolute;left:48px;top:70px;color:var(--white)}
.craft-title{font-size:38px;font-weight:500;line-height:1.5;letter-spacing:.1em}
.craft-en{font-size:15px;margin-top:12px;font-style:italic}
.craft-text{font-size:14px;line-height:2;margin-top:22px;letter-spacing:.06em}
.btn-outline-light{position:absolute;left:940px;top:290px;width:160px;height:42px;border:1px solid rgba(255,255,255,.8);color:var(--white);display:flex;align-items:center;justify-content:center;font-size:14px}

/* services */
.service{position:absolute;left:0;width:1200px;height:480px}
.service-title{position:absolute;writing-mode:vertical-rl;font-size:30px;font-weight:500;letter-spacing:.2em;line-height:1.5}
.service-title::before{content:"";position:absolute;top:-22px;right:-26px;width:16px;height:16px;background:var(--panel)}
.service-en{position:absolute;font-size:13px;color:var(--sub);font-style:italic}
.btn-view{position:absolute;width:150px;height:38px;border:1px solid var(--ink);display:flex;align-items:center;justify-content:center;font-size:13px}
.service-image{position:absolute}
.caption{position:absolute;font-size:10px;color:var(--sub);letter-spacing:.06em}
.img-mould{background:
    radial-gradient(ellipse 170px 120px at 32% 45%,rgba(214,200,176,.95),transparent 70%),
    radial-gradient(ellipse 160px 110px at 68% 55%,rgba(205,190,165,.9),transparent 70%),
    radial-gradient(ellipse 80px 60px at 45% 40%,rgba(255,252,245,.9),transparent 70%),
    linear-gradient(135deg,#f3f0e8,#ece6db)}
.img-sweets{background:
    radial-gradient(ellipse 130px 80px at 50% 50%,rgba(120,84,56,.95),transparent 75%),
    radial-gradient(ellipse 170px 110px at 50% 50%,rgba(154,112,78,.9),transparent 80%),
    linear-gradient(135deg,#ece9e2,#cfcac0)}
.img-festival{background:
    radial-gradient(ellipse 110px 150px at 62% 55%,rgba(70,64,68,.9),transparent 75%),
    radial-gradient(ellipse 70px 50px at 58% 26%,rgba(200,188,176,.9),transparent 75%),
    radial-gradient(ellipse 160px 80px at 65% 85%,rgba(150,144,150,.7),transparent 75%),
    linear-gradient(135deg,#f2efe8,#e0dbd2)}
.img-sign{background:
    radial-gradient(ellipse 60px 150px at 35% 52%,rgba(232,210,170,.95),transparent 80%),
    radial-gradient(ellipse 60px 150px at 65% 52%,rgba(232,210,170,.95),transparent 80%),
    radial-gradient(ellipse 30px 40px at 35% 30%,rgba(190,60,40,.55),transparent 80%),
    radial-gradient(ellipse 30px 40px at 65% 30%,rgba(190,60,40,.55),transparent 80%),
    linear-gradient(135deg,#f1eee6,#e6dfd2)}
.img-art{background:
    radial-gradient(ellipse 55px 50px at 40% 35%,rgba(250,248,244,1),transparent 80%),
    radial-gradient(ellipse 55px 50px at 62% 38%,rgba(250,248,244,1),transparent 80%),
    radial-gradient(ellipse 50px 45px at 45% 68%,rgba(250,248,244,1),transparent 80%),
    radial-gradient(ellipse 120px 110px at 50% 52%,rgba(205,196,182,.6),transparent 80%),
    linear-gradient(135deg,#f0ede6,#e4ddd1)}

/* news */
.topics{position:absolute;top:4380px;left:0;width:1200px;height:420px}
.topic-card{position:absolute;top:20px;width:304px}
.topic-photo{width:304px;height:180px}
.topic-label{font-size:14px;margin-top:14px;letter-spacing:.08em}
.topics-rule{position:absolute;left:116px;top:270px;width:968px;height:1px;background:var(--line)}
.news-head{position:absolute;left:116px;top:300px}
.news-head h2{font-size:22px;font-weight:500;letter-spacing:.2em}
.news-head .en{font-size:12px;color:var(--sub)}
.news-list{position:absolute;left:330px;top:296px;width:754px;list-style:none;font-size:13px}
.news-list li{display:flex;gap:28px;padding:10px 0;border-bottom:1px solid var(--line)}
.news-list .date{font-family:"Cormorant Garamond",serif;width:80px}
.news-list .cat{color:var(--key-dark);width:60px}

/* footer */
.site-footer{position:absolute;top:4800px;left:0;width:1200px;height:588px;border-top:1px solid var(--line)}
.footer-brand{position:absolute;left:0;width:1200px;top:40px;text-align:center}
.footer-brand .brand-name{font-size:30px}
.footer-brand .brand-en{font-size:12px}
.footer-address{position:absolute;left:0;width:1200px;top:112px;text-align:center;font-size:12px;color:var(--sub)}
.footer-tel{position:absolute;left:170px;top:160px;display:flex;align-items:center;gap:12px}
.footer-tel .num{font-family:"Cormorant Garamond",serif;font-size:34px;letter-spacing:.04em}
.footer-tel .hours{font-size:12px;color:var(--sub)}
.btn-mail{position:absolute;left:520px;top:165px;width:180px;height:46px;border:1px solid var(--ink);display:flex;align-items:center;justify-content:center;font-size:14px}
.btn-shop-lg{position:absolute;left:760px;top:165px;width:200px;height:46px;background:var(--key);color:var(--white);display:flex;align-items:center;justify-content:center;font-size:14px;letter-spacing:.12em}
.footer-nav{position:absolute;left:0;width:1200px;top:250px;display:flex;justify-content:center;gap:54px;font-size:13px;padding-top:22px;border-top:1px solid var(--line)}
.copyright{position:absolute;left:0;width:1200px;top:320px;text-align:center;font-size:11px;color:var(--sub)}
</style>
</head>
<body>

<header class="site-header">
  <div class="brand">
    <span class="brand-name">水瀬きがた</span>
    <span class="brand-en en">Minase Kigata</span>
  </div>
  <nav class="global-nav">
    <a href="#">ごあいさつ</a><a href="#">事業内容</a><a href="#">納入実績</a><a href="#">みなせのものづくり</a><a href="#">会社案内</a><a href="#">お問い合わせ</a>
  </nav>
  <a class="btn-shop en" href="#">ONLINE SHOP</a>
</header>

<section class="hero" role="img" aria-label="木型を削る職人の手元の写真">
  <div class="hero-copy">
    <h1 class="hero-title">木でつくる、<br>技でかたちにする</h1>
    <p class="hero-en en">Minase Kigata is a traditional craft from Minase, Hokkoku, Japan.<br>Turning wood into forms with advanced craftsmanship.</p>
  </div>
</section>

<section class="intro">
  <p class="intro-lead">北国の小京都 北国・水瀬<strong>水瀬きがた</strong><span class="en">Hokkoku Small Kyoto Minase</span></p>
  <div class="intro-photo" role="img" aria-label="工房に並ぶ木型の写真"></div>
  <p class="intro-text">水瀬きがたは、北国の小さな町で木型づくりを続けてまいりました。<br>一本の木から型を彫り出し、菓子や祭りの道具、看板などを形にしています。<br>職人の手仕事を大切にし、ひとつひとつ丁寧に仕上げております。<br>伝統の技と新しい発想で、皆さまの思いをかたちにいたします。</p>
</section>

<section class="craft" role="img" aria-label="木材を手で仕上げる職人の写真">
  <div class="craft-copy">
    <h2 class="craft-title">木工/木型職人技で<br>描いているものをかたちに</h2>
    <p class="craft-en en">Minase Kigata accepts production of original products.</p>
    <p class="craft-text">水瀬きがたでは、オーダーメイドでのご依頼を承っております。<br>イラストや図面をもとに、木の特性を生かした品をお作りします。<br>木材選びから仕上げまで、職人が責任をもって担当します。<br>ご相談やお見積りはお気軽に、お問い合わせ下さい。</p>
  </div>
  <a class="btn-outline-light en" href="#">Order</a>
</section>

<section class="service" style="top:1940px">
  <h3 class="service-title" style="left:300px;top:60px">木型木工</h3>
  <p class="service-en en" style="left:230px;top:250px">Wooden model Wood work</p>
  <a class="btn-view en" href="#" style="left:230px;top:290px">View</a>
  <div class="service-image img-mould" style="left:540px;top:0;width:540px;height:400px" role="img" aria-label="木で削り出した鋳物用の木型"></div>
  <p class="caption" style="left:990px;top:408px">木型の制作例</p>
</section>

<section class="service" style="top:2420px">
  <div class="service-image img-sweets" style="left:120px;top:40px;width:380px;height:380px" role="img" aria-label="花模様を彫った菓子木型"></div>
  <p class="caption" style="left:120px;top:428px">菓子木型の制作例</p>
  <h3 class="service-title" style="left:600px;top:50px">菓子木型</h3>
  <p class="service-en en" style="left:600px;top:240px">Japanese sweets wooden model</p>
  <a class="btn-view en" href="#" style="left:600px;top:280px">View</a>
</section>

<section class="service" style="top:2900px">
  <h3 class="service-title" style="left:330px;top:40px;font-size:28px">祭り<br>伝統芸能</h3>
  <p class="service-en en" style="left:230px;top:240px">Matsuri Performing Arts Association</p>
  <a class="btn-view en" href="#" style="left:230px;top:280px">View</a>
  <div class="service-image img-festival" style="left:540px;top:20px;width:540px;height:380px" role="img" aria-label="祭りの衣装と道具の写真"></div>
  <p class="caption" style="left:990px;top:408px">祭り道具の制作例</p>
</section>

<section class="service" style="top:3380px">
  <div class="service-image img-sign" style="left:120px;top:20px;width:380px;height:380px" role="img" aria-label="木製の看板サインの写真"></div>
  <p class="caption" style="left:120px;top:408px">看板の制作例</p>
  <h3 class="service-title" style="left:630px;top:40px;font-size:28px">看板<br>デザイン</h3>
  <p class="service-en en" style="left:600px;top:240px">Sign board Design</p>
  <a class="btn-view en" href="#" style="left:600px;top:280px">View</a>
</section>

<section class="service" style="top:3860px">
  <h3 class="service-title" style="left:330px;top:40px;font-size:28px">アート造形<br>彫刻</h3>
  <p class="service-en en" style="left:230px;top:250px">Art Molding Sculpture</p>
  <a class="btn-view en" href="#" style="left:230px;top:290px">View</a>
  <div class="service-image img-art" style="left:540px;top:20px;width:540px;height:380px" role="img" aria-label="木彫りの小さな造形作品の写真"></div>
  <p class="caption" style="left:990px;top:408px">造形の制作例</p>
</section>

<section class="topics">
  <div class="topic-card" style="left:116px">
    <div class="topic-photo" role="img" aria-label="作業場で木型を彫る様子" style="background:radial-gradient(ellipse 90px 60px at 40% 60%,rgba(220,190,150,.8),transparent 75%),linear-gradient(135deg,#4e3a2e,#8c6e54 60%,#5a4436)"></div>
    <p class="topic-label">角型木型職人の技</p>
  </div>
  <div class="topic-card" style="left:448px">
    <div class="topic-photo" role="img" aria-label="木製のスプーンの写真" style="background:radial-gradient(ellipse 40px 100px at 35% 55%,rgba(240,210,140,1),transparent 80%),radial-gradient(ellipse 40px 100px at 65% 50%,rgba(230,195,120,1),transparent 80%),linear-gradient(135deg,#d9b46e,#b98d45)"></div>
    <p class="topic-label">名入れ木製スプーンについて</p>
  </div>
  <div class="topic-card" style="left:780px">
    <div class="topic-photo" role="img" aria-label="木型で作った和菓子の写真" style="background:radial-gradient(ellipse 55px 50px at 32% 50%,rgba(250,245,245,1),transparent 80%),radial-gradient(ellipse 55px 50px at 68% 50%,rgba(250,245,245,1),transparent 80%),linear-gradient(135deg,#d2c4c6,#a9999c)"></div>
    <p class="topic-label">和菓子の木型をつくる</p>
  </div>
  <div class="topics-rule"></div>
  <div class="news-head">
    <h2>新着情報</h2>
    <p class="en">Information</p>
  </div>
  <ul class="news-list">
    <li><span class="date">2019.08.00</span><span class="cat">お知らせ</span><span>新商品を追加いたしました。</span></li>
    <li><span class="date">2019.08.00</span><span class="cat">メディア</span><span>雑誌に掲載されました。</span></li>
    <li><span class="date">2019.08.00</span><span class="cat">お知らせ</span><span>ホームページを公開しました。</span></li>
  </ul>
</section>

<footer class="site-footer">
  <div class="footer-brand">
    <div class="brand-name">水瀬きがた</div>
    <div class="brand-en en">Minase Kigata</div>
  </div>
  <p class="footer-address">〒000-0000 北国県水瀬市本町1-2-3</p>
  <div class="footer-tel">
    <svg width="26" height="26" viewBox="0 0 24 24" aria-hidden="true"><path d="M6.6 10.8a15 15 0 0 0 6.6 6.6l2.2-2.2a1 1 0 0 1 1-.25 11.4 11.4 0 0 0 3.6.57 1 1 0 0 1 1 1V20a1 1 0 0 1-1 1A17 17 0 0 1 3 4a1 1 0 0 1 1-1h3.5a1 1 0 0 1 1 1c0 1.25.2 2.45.57 3.6a1 1 0 0 1-.25 1z" fill="#2b2520"/></svg>
    <div><div class="num">0123-45-6789</div><div class="hours">9:00〜17:00</div></div>
  </div>
  <a class="btn-mail en" href="#">MAIL FORM</a>
  <a class="btn-shop-lg en" href="#">ONLINE SHOP</a>
  <nav class="footer-nav">
    <a href="#">ごあいさつ</a><a href="#">事業内容</a><a href="#">納入実績</a><a href="#">みなせのものづくり</a><a href="#">会社案内</a><a href="#">お問い合わせ</a>
  </nav>
  <p class="copyright en">© 2019 Minase Kigata</p>
</footer>

</body>
</html>
```